Business Stationery - Business Cards - Letterheads, Compliment Slips

We need a new set of artwork designed for our client, they are a Construction Company, that also sell Kitchens, bathrooms and appliances.
They are an up and comping company that focus on quality and bespoke build. For them it is all about the quality of what they install, build or design. They have recently been awarded sole distributorship of a German kitchen brand Annelore Kuchen.
We need to present a quick job to them and provide some proofs for their new Artwork which encompasses all the elements of the company
The company name is the Halvorn Group and we need to design a logo also.
Any Questions please let me know asap

Target Market(s)
Upmarket clients, or small Development companies.
Industry/Entity Type
Business
Look and feel

```html
<!DOCTYPE html>
<html lang="en">
<head>
<meta charset="utf-8">
<title>Halvorn Group — Stationery Proofs</title>
<link href="https://fonts.googleapis.com/css2?family=PT+Sans+Narrow&display=swap" rel="stylesheet">
<style>
  :root {
    --board: #d1d2d4;
    --paper: #ffffff;
    --brand-red: #ed1c24;
    --label-ink: #333333;
  }
  * { margin: 0; padding: 0; box-sizing: border-box; }
  html, body {
    width: 1200px;
    height: 1000px;
    overflow: hidden;
    background: var(--board);
  }
  .board {
    position: relative;
    width: 1200px;
    height: 1000px;
    background: var(--board);
    font-family: "PT Sans Narrow", "Arial Narrow", sans-serif;
  }
  .sheet {
    position: absolute;
    background: var(--paper);
  }
  .label {
    position: absolute;
    font-size: 13px;
    line-height: 1.3;
    text-transform: uppercase;
    color: var(--label-ink);
    letter-spacing: 0.2px;
  }
  .label--right { text-align: right; }

  .letterhead { width: 439px; height: 619px; top: 44px; }
  .letterhead--one { left: 155px; }
  .letterhead--two { left: 610px; }

  .logo-sheet { left: 155px; top: 692px; width: 280px; height: 278px; }

  .card { width: 209px; height: 144px; top: 723px; }
  .card--one { left: 603px; }
  .card--two { left: 836px; }

  .wordmark {
    position: absolute;
    display: flex;
    flex-direction: column;
    align-items: center;
    color: var(--brand-red);
    font-weight: 400;
    text-transform: uppercase;
    line-height: 1;
  }
  .wordmark__name { letter-spacing: 0.02em; }
  .wordmark__group { letter-spacing: 0.6em; margin-right: -0.6em; }

  .wordmark--hero { left: 0; right: 0; top: 58px; }
  .wordmark--hero .wordmark__name { font-size: 74px; }
  .wordmark--hero .wordmark__group { font-size: 28px; margin-top: 14px; }

  .wordmark--lh-top { right: 20px; top: 64px; }
  .wordmark--lh-top .wordmark__name { font-size: 16px; }
  .wordmark--lh-top .wordmark__group { font-size: 6px; margin-top: 3px; }

  .wordmark--lh-bottom { right: 24px; bottom: 32px; }
  .wordmark--lh-bottom .wordmark__name { font-size: 16px; }
  .wordmark--lh-bottom .wordmark__group { font-size: 6px; margin-top: 3px; }

  .wordmark--card-center { left: 0; right: 0; top: 44px; }
  .wordmark--card-center .wordmark__name { font-size: 22px; }
  .wordmark--card-center .wordmark__group { font-size: 8px; margin-top: 5px; }

  .wordmark--card-corner { left: 12px; top: 12px; }
  .wordmark--card-corner .wordmark__name { font-size: 12px; }
  .wordmark--card-corner .wordmark__group { font-size: 5px; margin-top: 2px; }
</style>
</head>
<body>
<main class="board">
  <p class="label label--right" style="right:1055px; top:44px;">Letterhead<br>Option 1</p>
  <section class="sheet letterhead letterhead--one">
    <div class="wordmark wordmark--lh-top">
      <span class="wordmark__name">Halvorn</span>
      <span class="wordmark__group">Group</span>
    </div>
  </section>

  <section class="sheet letterhead letterhead--two">
    <div class="wordmark wordmark--lh-bottom">
      <span class="wordmark__name">Halvorn</span>
      <span class="wordmark__group">Group</span>
    </div>
  </section>
  <p class="label" style="left:1063px; top:44px;">Option 2</p>

  <p class="label label--right" style="right:1055px; top:694px;">Logo</p>
  <section class="sheet logo-sheet">
    <div class="wordmark wordmark--hero">
      <span class="wordmark__name">Halvorn</span>
      <span class="wordmark__group">Group</span>
    </div>
  </section>

  <p class="label label--right" style="right:609px; top:722px;">Business Card<br>Option 1</p>
  <section class="sheet card card--one">
    <div class="wordmark wordmark--card-center">
      <span class="wordmark__name">Halvorn</span>
      <span class="wordmark__group">Group</span>
    </div>
  </section>

  <section class="sheet card card--two">
    <div class="wordmark wordmark--card-corner">
      <span class="wordmark__name">Halvorn</span>
      <span class="wordmark__group">Group</span>
    </div>
  </section>
  <p class="label" style="left:1055px; top:723px;">Option 2</p>
</main>
</body>
</html>
```